Enterprise Application UI beautification

We have an enterprise application that is being redesigned. A screenshot from the new UX/UI is provided. The current UI design is OK but we would like it to look better. The key goals of the UI are to look like a premium product (think luxury brand) and for it to be visually very appealing/attractive. When people see the UI we want them to have a significant, positive reaction. They should "ooh" and "ahh". This is a product sold to large enterprises, not consumers. The current UI is a little plain. The colors we want to use are blue, yellow, black, white and gray. We probably don't want different colors but feel free to use any variations within or close to that color scheme that you see fit. Also feel free to modify the spacing, icons, widgets, tables, fonts, etc.

Target Market(s)

Large enterprise customers (Summit 300).

Number of Pages Required

1 page

Font styles to use
Sans Serif

Colors
3277b5

Requirements
Must have
• A premium feel.

```html
<!DOCTYPE html>
<html lang="en">
<head>
<meta charset="utf-8">
<title>Data Sources</title>
<link href="https://fonts.googleapis.com/css2?family=Nunito+Sans:wght@400;600;700&display=swap" rel="stylesheet">
<style>
:root{
  --nav:#25303f;--ink:#2b3442;--muted:#8a94a3;--line:#e3e7ec;--bg:#f3f5f8;--panel:#ffffff;
  --teal:#17b39a;--red:#e84a3c;--blue:#3a5fe0;--amber:#f8ad3a;--grey:#b9c0c9;--head:#eef1f5;
}
*{box-sizing:border-box;margin:0;padding:0}
html,body{width:1200px;height:675px;overflow:hidden}
body{position:relative;background:var(--bg);font-family:'Nunito Sans',sans-serif;color:var(--ink)}
.abs{position:absolute}
.rail{left:0;top:0;width:62px;height:675px;background:var(--nav)}
.brand{left:0;top:22px;width:62px;text-align:center;color:#fff;font-weight:700;font-size:11px;letter-spacing:1px}
.rail-icon{left:19px;width:24px;height:24px;stroke:#c9d2dc;fill:none;stroke-width:1.5}
.rail-icon.on{stroke:var(--teal)}
.rail-mark{left:0;top:270px;width:3px;height:24px;background:var(--teal)}
.sources{left:62px;top:0;width:250px;height:675px;background:var(--panel)}
.sources h1{position:absolute;left:19px;top:20px;font-size:16.5px;font-weight:700}
.btn{display:flex;align-items:center;justify-content:center;gap:5px;color:#fff;border-radius:2px;font-weight:600;white-space:nowrap}
.add{left:175px;top:21px;width:57px;height:21px;background:var(--teal);font-size:10px}
.search{left:19px;top:64px;width:213px;height:34px;border:1px solid var(--line);border-radius:3px;box-shadow:0 1px 3px rgba(0,0,0,.06);font-size:10px;font-style:italic;color:var(--muted);padding:11px 15px}
.search svg{position:absolute;right:14px;top:9px}
.list{left:0;top:121px;width:241px}
.item{position:relative;height:56px;border-bottom:1px solid var(--line);padding:12px 0 0 38px}
.item.on{background:#f1f3f5;border-left:3px solid var(--teal);padding-left:35px}
.item .dot{position:absolute;left:20px;top:17px;width:9px;height:9px;border-radius:50%}
.item.on .dot{left:17px}
.item b{display:block;font-weight:400;font-size:11.5px}
.item span{display:block;font-size:9px;color:var(--teal);margin-top:3px}
.g{background:var(--teal)}.r{background:var(--red)}.n{background:var(--grey)}
.scroll{left:308px;top:121px;width:4px;height:554px;background:#eceef1}
.scroll i{display:block;height:87px;background:#c4c9cf}
.user{left:1092px;top:14px;font-size:12px;display:flex;align-items:center;gap:6px}
.card{left:337px;top:48px;width:838px;height:188px;background:var(--panel);border-radius:6px;box-shadow:0 2px 8px rgba(30,40,60,.05)}
.card .status{left:14px;top:21px;width:10px;height:10px;border-radius:50%;background:var(--teal)}
.card h2{position:absolute;left:33px;top:11px;font-size:19.5px;font-weight:700}
.actions{right:12px;top:13px;display:flex;gap:19px}
.actions .btn{height:25px;padding:0 9px;font-size:12px;font-weight:400}
.rule{left:14px;right:12px;top:50px;height:1px;background:var(--line)}
.meta{top:61px;left:13px}
.meta dl{position:absolute;width:300px}
.meta dt{font-size:9px;color:var(--teal)}
.meta dt.lg{font-size:11px}
.meta dd{font-size:11.5px;margin-top:2px}
.section-title{left:337px;top:256px;font-size:19.5px;font-weight:600}
.obj{left:337px;width:838px;background:var(--panel);border-radius:4px;box-shadow:0 2px 6px rgba(30,40,60,.06)}
.obj-head{height:38px;display:flex;align-items:center;padding-left:32px;font-size:13px;font-weight:600;position:relative}
.obj-head .chev{position:absolute;left:12px;top:15px}
.obj.open .obj-head{background:var(--nav);color:#fff;border-radius:4px 4px 0 0}
.obj-tools{position:absolute;right:8px;top:8px;display:flex;gap:9px}
.obj-tools .btn{height:22px;padding:0 7px;font-size:11.5px;font-weight:400}
table{width:100%;border-collapse:collapse}
th{background:var(--head);height:36px;text-align:left;font-size:11.5px;font-weight:600;padding-left:13px}
td{height:34px;font-size:10px;padding-left:13px;border-bottom:1px solid var(--line);color:#4a5260}
tr:last-child td{border-bottom:none}
.icons{display:flex;align-items:center;gap:10px}
.icons svg{stroke:#9aa2ad;fill:none;stroke-width:1.2}
.icons .a{font-size:15px;color:#9aa2ad;font-weight:600;line-height:1;margin-top:-3px}
.icons .dark{stroke:#333b47}.a.dark{color:#222}
.icons .tl{stroke:var(--teal)}.a.tl{color:var(--teal)}
.chk{display:inline-block;width:14px;height:14px;background:#d3d8de;border:1px solid #bfc6ce;margin-left:27px}
.chk.on{background:#dbe7f5;border-color:#5d88c4}
</style>
</head>
<body>
<nav class="abs rail">
  <div class="abs brand">ARCIS</div>
  <svg class="abs rail-icon" style="top:116px" viewBox="0 0 24 24"><circle cx="12" cy="8" r="3"/><circle cx="5" cy="7" r="2"/><circle cx="19" cy="7" r="2"/><path d="M6 20v-5a6 6 0 0 1 12 0v5M2 18v-4a3 3 0 0 1 3-3M22 18v-4a3 3 0 0 0-3-3"/></svg>
  <svg class="abs rail-icon" style="top:192px" viewBox="0 0 24 24"><path d="M6 18h12a4 4 0 0 0 0-8 6 6 0 0 0-11.5-1A4.5 4.5 0 0 0 6 18z"/></svg>
  <div class="abs rail-mark"></div>
  <svg class="abs rail-icon on" style="top:270px" viewBox="0 0 24 24"><rect x="4" y="3" width="14" height="14" rx="1"/><path d="M7 20h14V7M7 7h8M7 11h8"/></svg>
  <svg class="abs rail-icon" style="top:347px" viewBox="0 0 24 24"><rect x="5" y="4" width="14" height="17" rx="2"/><path d="M9 3h6v3H9zM8 11h8M8 15h5"/></svg>
  <svg class="abs rail-icon" style="top:425px" viewBox="0 0 24 24"><rect x="3" y="5" width="17" height="15" rx="2"/><path d="M3 9h17M8 3v4M15 3v4"/><circle cx="17" cy="17" r="3.5"/></svg>
  <svg class="abs rail-icon" style="top:503px" viewBox="0 0 24 24"><circle cx="6" cy="5" r="2.5"/><circle cx="18" cy="19" r="2.5"/><path d="M6 8v5a4 4 0 0 0 4 4h5M18 16v-5a4 4 0 0 0-4-4H9"/></svg>
</nav>

<aside class="abs sources">
  <h1>Data Sources</h1>
  <div class="abs btn add"><svg width="10" height="10" viewBox="0 0 10 10" stroke="#fff" stroke-width="1.6"><path d="M5 0v10M0 5h10"/></svg>ADD</div>
  <div class="abs search">Search Data Sources...<svg width="15" height="15" viewBox="0 0 16 16" fill="none" stroke="#17b39a" stroke-width="1.8"><circle cx="7" cy="7" r="5.5"/><path d="M11 11l4 4"/></svg></div>
  <div class="abs list">
    <div class="item on"><i class="dot g"></i><b>Cloudforge - Sandbox</b><span>cloudforge.io</span></div>
    <div class="item"><i class="dot g"></i><b>Relata Test 1 (administration)</b><span>RelataSQL</span></div>
    <div class="item"><i class="dot g"></i><b>Relata Test 2 (administration)</b><span>RelataSQL</span></div>
    <div class="item"><i class="dot r"></i><b>Sadge</b><span>cloudforge.io</span></div>
    <div class="item"><i class="dot n"></i><b>Cloudforge Test 1 (masterd ev)</b><span>RelataSQL</span></div>
    <div class="item"><i class="dot n"></i><b>CFDC - Field Entry Test</b><span>cloudforge.io</span></div>
    <div class="item"><i class="dot g"></i><b>CFDC 44</b><span>cloudforge.io</span></div>
    <div class="item"><i class="dot r"></i><b>CFDC 66</b><span>cloudforge.io</span></div>
    <div class="item"><i class="dot r"></i><b>CFDC - Field Entry Test</b><span>cloudforge.io</span></div>
  </div>
</aside>
<div class="abs scroll"><i></i></div>

<div class="abs user"><svg width="13" height="13" viewBox="0 0 24 24" fill="none" stroke="#2b3442" stroke-width="1.8"><circle cx="12" cy="12" r="3.5"/><path d="M12 2v3M12 19v3M2 12h3M19 12h3M4.9 4.9l2.1 2.1M17 17l2.1 2.1M4.9 19.1L7 17M17 7l2.1-2.1"/></svg>Dana Royce<svg width="9" height="9" viewBox="0 0 10 10" fill="none" stroke="#2b3442" stroke-width="1.4"><path d="M1 3l4 4 4-4"/></svg></div>

<section class="abs card">
  <i class="abs status"></i>
  <h2>Cloudforge - Sandbox</h2>
  <div class="abs actions">
    <div class="btn" style="background:var(--teal)"><svg width="13" height="13" viewBox="0 0 16 16" fill="none" stroke="#fff" stroke-width="1.3"><path d="M2 14l1-4 8-8 3 3-8 8zM10 3l3 3"/></svg>Edit</div>
    <div class="btn" style="background:var(--blue)"><svg width="13" height="13" viewBox="0 0 16 16" fill="none" stroke="#fff" stroke-width="1.4"><circle cx="7" cy="9" r="5"/><circle cx="11" cy="5" r="3"/></svg>Clone</div>
    <div class="btn" style="background:var(--red)"><svg width="13" height="13" viewBox="0 0 16 16" fill="none" stroke="#fff" stroke-width="1.3"><circle cx="8" cy="8" r="6.5"/><path d="M5.5 5.5l5 5M10.5 5.5l-5 5"/></svg>Remove</div>
    <div class="btn" style="background:var(--amber)"><svg width="12" height="13" viewBox="0 0 12 16" fill="none" stroke="#fff" stroke-width="1.2"><path d="M7 1L2 9h4l-1 6 5-8H6z"/></svg>Test Connection</div>
  </div>
  <div class="abs rule"></div>
  <div class="abs meta">
    <dl style="left:10px;top:0"><dt>Production</dt><dd>Production Company Name</dd></dl>
    <dl style="left:10px;top:44px"><dt>Created By</dt><dd>halvern.test</dd></dl>
    <dl style="left:10px;top:88px"><dt>Last Updated By</dt><dd>halvern.test</dd></dl>
    <dl style="left:334px;top:-1px"><dt class="lg">Date Source Name</dt><dd>Application</dd></dl>
    <dl style="left:334px;top:44px"><dt>Status</dt><dd>Active</dd></dl>
    <dl style="left:334px;top:88px"><dt>Date Source Name</dt><dd>halvern.test</dd></dl>
    <dl style="left:598px;top:0"><dt>User Name</dt><dd>masterdev@dev.nimbusdata.io</dd></dl>
    <dl style="left:598px;top:44px"><dt>Security Type</dt><dd>tadkaji4234ifndkn3</dd></dl>
    <dl style="left:598px;top:88px"><dt>Connected App</dt><dd>No ?</dd></dl>
  </div>
</section>

<h3 class="abs section-title">Data Objects</h3>

<section class="abs obj open" style="top:293px">
  <div class="obj-head"><svg class="chev" width="12" height="8" viewBox="0 0 12 8" fill="none" stroke="#17b39a" stroke-width="1.6"><path d="M1 7l5-5 5 5"/></svg>Account
    <div class="obj-tools">
      <div class="btn" style="background:var(--red)"><svg width="13" height="13" viewBox="0 0 16 16"><circle cx="8" cy="8" r="7.5" fill="#fff"/><path d="M5.5 5.5l5 5M10.5 5.5l-5 5" stroke="#e84a3c" stroke-width="1.6"/></svg>Remove Object</div>
      <div class="btn" style="background:var(--teal)"><svg width="13" height="13" viewBox="0 0 16 16"><circle cx="8" cy="8" r="7.5" fill="#fff"/><path d="M8 4.5v7M4.5 8h7" stroke="#17b39a" stroke-width="1.6"/></svg>Add Filds</div>
    </div>
  </div>
  <table>
    <colgroup><col style="width:187px"><col style="width:184px"><col style="width:155px"><col style="width:113px"><col style="width:126px"><col></colgroup>
    <tr><th>Field Name</th><th>Data Type</th><th>Rule Types</th><th>Primary Key</th><th>Sensitive Data</th><th>Actions</th></tr>
    <tr><td>Account Description</td><td>Common Text</td>
      <td><div class="icons"><span class="a dark">a</span><svg width="12" height="12" viewBox="0 0 12 12"><circle cx="5" cy="5" r="4"/><path d="M8 8l3 3"/></svg><svg class="dark" width="12" height="12" viewBox="0 0 12 12"><rect x="1" y="3" width="8" height="8"/><path d="M3 1h8v8"/></svg><svg width="12" height="12" viewBox="0 0 12 12"><path d="M6 1l5 9H1z"/></svg><svg width="12" height="12" viewBox="0 0 12 12"><circle cx="6" cy="6" r="4"/><path d="M6 0v3M6 9v3M0 6h3M9 6h3"/></svg><svg width="6" height="8" viewBox="0 0 6 8"><path d="M0 0l5 4-5 4z" fill="#9aa2ad" stroke="none"/></svg></div></td>
      <td><span class="chk on"></span></td>
      <td><div class="icons" style="gap:22px"><svg width="10" height="12" viewBox="0 0 10 12"><rect x="1" y="2" width="8" height="9"/><path d="M3 1h4M5 4v5M3 6.5h4"/></svg><svg width="15" height="10" viewBox="0 0 15 10"><rect x="1" y="1" width="13" height="8"/><path d="M3 6h4"/></svg><svg width="11" height="12" viewBox="0 0 11 12"><circle cx="5.5" cy="4" r="3"/><path d="M1 11c0-3 9-3 9 0z"/></svg></div></td>
      <td><div class="icons" style="gap:16px"><svg width="14" height="14" viewBox="0 0 14 14"><path d="M1 13l1-3 8-8 2 2-8 8zM9 3l2 2"/></svg><svg width="14" height="14" viewBox="0 0 14 14"><circle cx="7" cy="7" r="6.5" fill="#9aa2ad" stroke="none"/><path d="M4.5 4.5l5 5M9.5 4.5l-5 5" stroke="#fff" stroke-width="1.4"/></svg></div></td></tr>
    <tr><td>Account Fax</td><td>Address. Address Line 3</td>
      <td><div class="icons"><span class="a">a</span><svg width="12" height="12" viewBox="0 0 12 12"><circle cx="5" cy="5" r="4"/><path d="M8 8l3 3"/></svg><svg class="dark" width="12" height="12" viewBox="0 0 12 12"><rect x="1" y="3" width="8" height="8"/><path d="M3 1h8v8"/></svg><svg width="12" height="12" viewBox="0 0 12 12"><path d="M6 1l5 9H1z"/></svg><svg width="12" height="12" viewBox="0 0 12 12"><circle cx="6" cy="6" r="4"/><path d="M6 0v3M6 9v3M0 6h3M9 6h3"/></svg><svg width="6" height="8" viewBox="0 0 6 8"><path d="M0 0l5 4-5 4z" fill="#9aa2ad" stroke="none"/></svg></div></td>
      <td><span class="chk"></span></td><td></td>
      <td><div class="icons" style="gap:16px"><svg width="14" height="14" viewBox="0 0 14 14"><path d="M1 13l1-3 8-8 2 2-8 8zM9 3l2 2"/></svg><svg width="14" height="14" viewBox="0 0 14 14"><circle cx="7" cy="7" r="6.5" fill="#9aa2ad" stroke="none"/><path d="M4.5 4.5l5 5M9.5 4.5l-5 5" stroke="#fff" stroke-width="1.4"/></svg></div></td></tr>
    <tr><td>Account ID</td><td>Common ID</td>
      <td><div class="icons"><span class="a tl">a</span><svg class="tl" width="12" height="12" viewBox="0 0 12 12"><circle cx="5" cy="5" r="4"/><path d="M8 8l3 3"/></svg><svg width="12" height="12" viewBox="0 0 12 12"><rect x="1" y="3" width="8" height="8"/><path d="M3 1h8v8"/></svg><svg width="12" height="12" viewBox="0 0 12 12"><path d="M6 1l5 9H1z"/></svg><svg width="12" height="12" viewBox="0 0 12 12"><circle cx="6" cy="6" r="4"/><path d="M6 0v3M6 9v3M0 6h3M9 6h3"/></svg><svg width="6" height="8" viewBox="0 0 6 8"><path d="M0 0l5 4-5 4z" fill="#9aa2ad" stroke="none"/></svg></div></td>
      <td><span class="chk"></span></td>
      <td><div class="icons" style="gap:22px"><svg width="10" height="12" viewBox="0 0 10 12"><rect x="1" y="2" width="8" height="9"/><path d="M3 1h4M5 4v5M3 6.5h4"/></svg><svg width="15" height="10" viewBox="0 0 15 10"><rect x="1" y="1" width="13" height="8"/><path d="M3 6h4"/></svg><svg width="11" height="12" viewBox="0 0 11 12"><circle cx="5.5" cy="4" r="3"/><path d="M1 11c0-3 9-3 9 0z"/></svg></div></td>
      <td><div class="icons" style="gap:16px"><svg width="14" height="14" viewBox="0 0 14 14"><path d="M1 13l1-3 8-8 2 2-8 8zM9 3l2 2"/></svg><svg width="14" height="14" viewBox="0 0 14 14"><circle cx="7" cy="7" r="6.5" fill="#9aa2ad" stroke="none"/><path d="M4.5 4.5l5 5M9.5 4.5l-5 5" stroke="#fff" stroke-width="1.4"/></svg></div></td></tr>
    <tr><td>Account Name</td><td>Address. Address Line 2</td>
      <td><div class="icons"><span class="a">a</span><svg width="12" height="12" viewBox="0 0 12 12"><circle cx="5" cy="5" r="4"/><path d="M8 8l3 3"/></svg><svg class="dark" width="12" height="12" viewBox="0 0 12 12"><rect x="1" y="3" width="8" height="8"/><path d="M3 1h8v8"/></svg><svg width="12" height="12" viewBox="0 0 12 12"><path d="M6 1l5 9H1z"/></svg><svg width="12" height="12" viewBox="0 0 12 12"><circle cx="6" cy="6" r="4"/><path d="M6 0v3M6 9v3M0 6h3M9 6h3"/></svg><svg width="6" height="8" viewBox="0 0 6 8"><path d="M0 0l5 4-5 4z" fill="#9aa2ad" stroke="none"/></svg></div></td>
      <td><span class="chk"></span></td><td></td>
      <td><div class="icons" style="gap:16px"><svg width="14" height="14" viewBox="0 0 14 14"><path d="M1 13l1-3 8-8 2 2-8 8zM9 3l2 2"/></svg><svg width="14" height="14" viewBox="0 0 14 14"><circle cx="7" cy="7" r="6.5" fill="#9aa2ad" stroke="none"/><path d="M4.5 4.5l5 5M9.5 4.5l-5 5" stroke="#fff" stroke-width="1.4"/></svg></div></td></tr>
  </table>
</section>

<section class="abs obj" style="top:516px"><div class="obj-head"><svg class="chev" width="12" height="8" viewBox="0 0 12 8" fill="none" stroke="#2b3442" stroke-width="1.6"><path d="M1 1l5 5 5-5"/></svg>Asset</div></section>
<section class="abs obj" style="top:566px"><div class="obj-head"><svg class="chev" width="12" height="8" viewBox="0 0 12 8" fill="none" stroke="#2b3442" stroke-width="1.6"><path d="M1 1l5 5 5-5"/></svg>Asset Relationship</div></section>
<section class="abs obj" style="top:616px"><div class="obj-head"><svg class="chev" width="12" height="8" viewBox="0 0 12 8" fill="none" stroke="#2b3442" stroke-width="1.6"><path d="M1 1l5 5 5-5"/></svg>Asset Token Event</div></section>
</body>
</html>
```